Webdesign für Betreiber einer Windkraftanlage
Zielgruppe
Helix Windkraftanlage und Informationsübertragung
Aufgabenstellung
Hi, we are looking for a new home page for our company 'varomind', our company is about developing helix wind and solar power plants and wireless data transmitting tech.
The main landing page should consist of something like a honeycomb as seen on our drawing and the example printet flyer. In the middle a 'varomind' logo or something like this, and the 6 categories around: 1. Smart City 2. Kommunikation (Katastrophenschutz, Zivilschutz) 3. Sport-Freizeit 4. Defence 5. Umwelt Agrar Land&Forstwirtschaft 6. F&E Forschung und Entwicklung
We have one home page already, still the old name and a lot of our ideas changed, business purpose etc. but to give you an idea: www.qt7r.at

```html
<!DOCTYPE html>
<html lang="de">
<head>
<meta charset="utf-8">
<title>varomind – Erneuerbare Energie</title>
<link rel="stylesheet" href="https://fonts.googleapis.com/css2?family=Roboto:wght@400;500;700&display=swap">
<style>
:root{
  --ink:#0f172a;
  --text:#374151;
  --muted:#6b7280;
  --blue:#00b4ff;
  --green-dot:#22c55e;
  --light:#f8f9fb;
  --dark:#141c2f;
  --c-city:#00bfff;
  --c-comm:#ff4500;
  --c-sport:#ffd700;
  --c-def:#2f4f4f;
  --c-env:#228b22;
  --c-rd:#6a5acd;
  --line:#e5e7eb;
}
*{box-sizing:border-box;margin:0;padding:0}
html,body{width:1200px;height:4579px;overflow:hidden}
body{font-family:"Roboto",Arial,sans-serif;color:var(--text);background:#fff;position:relative}
.nav{position:absolute;top:0;left:0;width:1200px;height:55px;display:flex;align-items:center;justify-content:space-between;padding:0 80px;background:rgba(255,255,255,.95);z-index:2}
.brand{font-weight:700;font-size:32px;color:var(--ink);letter-spacing:-.5px;display:flex;align-items:center;gap:8px}
.brand-dot{width:12px;height:12px;border-radius:50%;background:var(--blue)}
.nav ul{list-style:none;display:flex;gap:28px;font-size:13px;color:var(--ink)}
.hero{position:absolute;top:0;left:0;width:1200px;height:852px;background:linear-gradient(180deg,#fff 0%,#f4f7fa 100%);text-align:center;overflow:hidden}
.hero-panel{position:absolute;left:770px;top:480px;width:440px;height:300px;background:linear-gradient(150deg,#eef4fa 0%,#7fa4cf 45%,#2c5fa3 75%,#dbe6f1 100%);clip-path:polygon(30% 0,100% 0,100% 80%,62% 100%,0 65%);opacity:.85}
.hero h1{position:absolute;top:318px;left:0;width:1200px;font-size:48px;line-height:52px;font-weight:700;color:var(--ink)}
.hero p{position:absolute;top:444px;left:0;width:1200px;font-size:19px;line-height:27px;color:#333}
.btn{display:inline-flex;align-items:center;gap:8px;background:var(--blue);color:#fff;font-size:14px;font-weight:500;border-radius:5px;padding:0 22px;height:48px}
.btn .dot{width:13px;height:13px;border-radius:50%;background:var(--green-dot)}
.hero .btn{position:absolute;top:531px;left:507px;width:186px;justify-content:center}
.core{position:absolute;top:852px;left:0;width:1200px;height:1173px;background:var(--light)}
.core h2,.apps h2{text-align:center;font-size:28px;font-weight:700;color:var(--ink)}
.core h2{margin-top:66px}
.grid{position:absolute;top:153px;left:185px;display:grid;grid-template-columns:repeat(3,272px);grid-auto-rows:313px;gap:8px}
.tile{display:flex;flex-direction:column;align-items:center;justify-content:center;text-align:center;color:#fff;padding:0 38px}
.tile svg{width:24px;height:24px;margin-bottom:18px;stroke:#fff;fill:none;stroke-width:1.7}
.tile h3{font-size:17px;font-weight:700;margin-bottom:10px}
.tile p{font-size:11.5px;line-height:17px}
.t-city{background:var(--c-city)}.t-comm{background:var(--c-comm)}
.t-sport{background:var(--c-sport)}.t-sport p{color:#fff8c0}
.t-core{background:#fff;color:var(--ink);font-weight:700;font-size:12px}
.t-def{background:var(--c-def)}.t-env{background:var(--c-env)}.t-rd{background:var(--c-rd)}
.feature{position:absolute;left:0;width:1200px}
.helix{top:2025px;height:555px;background:#fff}
.data{top:2580px;height:555px;background:var(--light)}
.feature h2{font-size:29px;line-height:35px;font-weight:700;color:var(--ink);margin-bottom:24px}
.feature .copy{position:absolute;width:500px}
.feature .copy>p{font-size:14px;line-height:23px;margin-bottom:22px}
.checks{list-style:none;margin-bottom:30px}
.checks li{display:flex;align-items:center;gap:14px;font-size:12.5px;margin-bottom:20px}
.checks svg{width:15px;height:15px;stroke:var(--blue);fill:none;stroke-width:2}
.feature .btn{height:38px;font-size:13px;padding:0 20px}
.media{position:absolute;width:500px;height:420px;border-radius:10px;box-shadow:0 10px 25px rgba(0,0,0,.12)}
.helix .copy{left:80px;top:100px}
.helix .media{left:620px;top:67px;background:radial-gradient(circle at 50% 50%,#fafafa 0%,#dcdcdc 60%,#c8c8c8 100%)}
.data .copy{left:620px;top:90px}
.data .media{left:80px;top:65px;background:linear-gradient(180deg,#0b0b0b 0%,#6b6b6b 45%,#fff 75%)}
.apps{position:absolute;top:3135px;left:0;width:1200px;height:715px;background:#fff}
.apps h2{margin-top:62px}
.app-grid{position:absolute;top:142px;left:80px;display:grid;grid-template-columns:repeat(3,330px);grid-auto-rows:250px;gap:40px 25px}
.app{background:#fff;border-radius:10px;box-shadow:0 4px 14px rgba(0,0,0,.07);text-align:center;padding:30px 34px}
.app .ico{width:52px;height:52px;border-radius:50%;margin:0 auto 24px;display:flex;align-items:center;justify-content:center}
.app .ico svg{width:22px;height:22px;fill:none;stroke-width:1.7}
.app h3{font-size:16px;font-weight:700;color:var(--ink);margin-bottom:18px}
.app p{font-size:12.5px;line-height:20px;color:var(--muted)}
.cta{position:absolute;top:3850px;left:0;width:1200px;height:323px;background:var(--dark);text-align:center;color:#fff}
.cta h2{margin-top:80px;font-size:29px;font-weight:700}
.cta p{margin-top:24px;font-size:16px;line-height:24px;color:#d8dde6}
.cta .btn{margin-top:28px;width:186px;justify-content:center}
.footer{position:absolute;top:4173px;left:0;width:1200px;height:406px;background:#f4f5f7;padding:0 80px}
.footer .fbrand{position:absolute;top:50px;left:80px;font-size:19px;font-weight:700;color:var(--ink)}
.social{position:absolute;top:43px;right:80px;display:flex;gap:20px}
.social span{width:34px;height:34px;border-radius:50%;background:#e6e8ec}
.cols{position:absolute;top:108px;left:80px;display:grid;grid-template-columns:repeat(4,266px)}
.cols h4{font-size:14px;font-weight:700;color:var(--ink);margin-bottom:18px}
.cols li{list-style:none;font-size:12.5px;color:var(--muted);margin-bottom:10px;line-height:17px}
.contact li{display:flex;gap:8px}
.contact svg{width:13px;height:13px;stroke:var(--blue);fill:none;stroke-width:1.8;flex:none;margin-top:2px}
.legal{position:absolute;top:4540px;left:80px;width:1040px;display:flex;justify-content:space-between;font-size:12px;color:var(--muted)}
.legal span+span{margin-left:20px}
.theme{position:absolute;top:4522px;left:1148px;width:36px;height:36px;border-radius:50%;background:#fff;box-shadow:0 2px 8px rgba(0,0,0,.12)}
</style>
</head>
<body>
<header class="nav">
  <div class="brand">varomind<span class="brand-dot"></span></div>
  <ul><li>Home</li><li>Solutions</li><li>Technology</li><li>About</li><li>Contact</li></ul>
</header>

<section class="hero">
  <div class="hero-panel" role="img" aria-label="Solarmodulfeld vor Windturbinen im Dunst"></div>
  <h1>Die Zukunft der erneuerbaren Energie<br>gestalten</h1>
  <p>Innovative Helix-Wind- und Solarenergiesysteme kombiniert mit<br>drahtloser Datenübertragung für eine nachhaltige Zukunft</p>
  <span class="btn"><span class="dot"></span>Jetzt entdecken</span>
</section>

<section class="core">
  <h2>Unsere Kernbereiche</h2>
  <div class="grid">
    <div class="tile t-city"><svg viewBox="0 0 24 24"><rect x="5" y="3" width="14" height="18"/><path d="M9 7h2M13 7h2M9 11h2M13 11h2M9 15h2M13 15h2"/></svg><h3>Smart City</h3><p>Intelligente städtische Infrastrukturlösungen mit erneuerbaren Energien</p></div>
    <div class="tile t-comm"><svg viewBox="0 0 24 24"><circle cx="12" cy="11" r="2"/><path d="M12 13v8M7.5 6.5a6 6 0 000 9M16.5 6.5a6 6 0 010 9M4.5 3.5a10 10 0 000 15M19.5 3.5a10 10 0 010 15"/></svg><h3>Kommunikation</h3><p>Civil protection and disaster management communication systems</p></div>
    <div class="tile t-sport"><svg viewBox="0 0 24 24"><circle cx="12" cy="12" r="9"/><path d="M3 12h18M12 3c3 3 3 15 0 18M12 3c-3 3-3 15 0 18"/></svg><h3>Sport &amp; Freizeit</h3><p>Nachhaltige Energielösungen für Sportanlagen und Freizeitbereiche</p></div>
    <div class="tile t-core">varomind</div>
    <div class="tile t-def"><svg viewBox="0 0 24 24"><path d="M12 3l7 3v6c0 4-3 7-7 9-4-2-7-5-7-9V6z"/></svg><h3>Verteidigung</h3><p>Zuverlässige Energie- und Kommunikationslösungen für Verteidigungsanwendungen</p></div>
    <div class="tile t-env"><svg viewBox="0 0 24 24"><path d="M12 21v-9M12 12c0-4-3-6-7-6 0 4 3 6 7 6zM12 12c0-4 3-6 7-6 0 4-3 6-7 6zM7 21h10"/></svg><h3>Umwelt &amp; Agrar</h3><p>Umweltüberwachung und Agrartechnologie mit sauberer Energie</p></div>
    <div class="tile t-rd"><svg viewBox="0 0 24 24"><path d="M9 3h6M10 3v6l-5 11h14l-5-11V3"/></svg><h3>Forschung &amp; Entwicklung</h3><p>Modernste Forschung und Entwicklung im Bereich erneuerbarer Energietechnologien</p></div>
  </div>
</section>

<section class="feature helix">
  <div class="copy">
    <h2>Revolutionäre Helix-<br>Windtechnologie</h2>
    <p>Unsere patentierten Helix-Windturbinen gewinnen Energie aus allen Windrichtungen mit maximaler Effizienz, selbst bei schwachem Wind. In Kombination mit modernen Solarmodulen liefern unsere Hybridsysteme überall zuverlässige, nachhaltige Energie.</p>
    <ul class="checks">
      <li><svg viewBox="0 0 16 16"><path d="M3 8l3 3 7-7"/></svg>Effizient bei niedrigen Windgeschwindigkeiten (ab 2 m/s)</li>
      <li><svg viewBox="0 0 16 16"><path d="M3 8l3 3 7-7"/></svg>Omnidirektionales Design nutzt Wind aus allen Richtungen</li>
      <li><svg viewBox="0 0 16 16"><path d="M3 8l3 3 7-7"/></svg>Hybrid-Solarintegration für kontinuierliche Energieerzeugung</li>
    </ul>
    <span class="btn">Mehr erfahren</span>
  </div>
  <div class="media" role="img" aria-label="Weiße Windturbine in einem Ring mit gebogenem Solarmodul"></div>
</section>

<section class="feature data">
  <div class="media" role="img" aria-label="Funkmast mit Solarmodulen und kreisförmigen Signalwellen"></div>
  <div class="copy">
    <h2>Integrierte drahtlose<br>Datenübertragung</h2>
    <p>Unsere Systeme erzeugen nicht nur Energie - sie schaffen Kommunikationsnetzwerke. Jede Installation dient als Knoten in einem robusten drahtlosen Mesh-Netzwerk und ermöglicht die Datenübertragung auch an abgelegenen Orten oder in Notfallsituationen.</p>
    <ul class="checks">
      <li><svg viewBox="0 0 16 16"><path d="M3 8l3 3 7-7"/></svg>Self-powered communication infrastructure</li>
      <li><svg viewBox="0 0 16 16"><path d="M3 8l3 3 7-7"/></svg>Mesh network capability for extended coverage</li>
      <li><svg viewBox="0 0 16 16"><path d="M3 8l3 3 7-7"/></svg>Encrypted, secure data transmission protocols</li>
    </ul>
    <span class="btn">Discover Technology</span>
  </div>
</section>

<section class="apps">
  <h2>Anwendungen in verschiedenen Branchen</h2>
  <div class="app-grid">
    <div class="app"><div class="ico" style="background:#e0f6ff"><svg viewBox="0 0 24 24" stroke="#00bfff"><rect x="5" y="3" width="14" height="18"/><path d="M9 7h2M13 7h2M9 11h2M13 11h2M9 15h2M13 15h2"/></svg></div><h3>Smart City Infrastruktur</h3><p>Versorgung von intelligenter Straßenbeleuchtung, Verkehrsmanagementsystemen und öffentlichen WLAN-Netzen mit sauberer, erneuerbarer Energie.</p></div>
    <div class="app"><div class="ico" style="background:#ffe6dc"><svg viewBox="0 0 24 24" stroke="#ff4500"><path d="M6 20h12M8 20v-6a4 4 0 018 0v6M12 4v2M5 7l1.5 1.5M19 7l-1.5 1.5"/></svg></div><h3>Emergency Response</h3><p>Rapidly deployable communication systems for disaster zones and emergency situations where grid power is unavailable.</p></div>
    <div class="app"><div class="ico" style="background:#fff8d6"><svg viewBox="0 0 24 24" stroke="#f5c400"><circle cx="12" cy="12" r="9"/><path d="M3 12h18M12 3c3 3 3 15 0 18M12 3c-3 3-3 15 0 18"/></svg></div><h3>Sports Facilities</h3><p>Sustainable power solutions for stadiums, training grounds, and outdoor areas with integrated data services.</p></div>
    <div class="app"><div class="ico" style="background:#e3e8e8"><svg viewBox="0 0 24 24" stroke="#2f4f4f"><path d="M12 3l7 3v6c0 4-3 7-7 9-4-2-7-5-7-9V6z"/></svg></div><h3>Defense Applications</h3><p>Secure, off-grid power and communication systems for remote outposts and tactical deployments.</p></div>
    <div class="app"><div class="ico" style="background:#e2f2e2"><svg viewBox="0 0 24 24" stroke="#228b22"><path d="M12 21v-9M12 12c0-4-3-6-7-6 0 4 3 6 7 6zM12 12c0-4 3-6 7-6 0 4-3 6-7 6zM7 21h10"/></svg></div><h3>Agricultural Monitoring</h3><p>Self-powered sensor networks for crop monitoring, irrigation management, and environmental data collection.</p></div>
    <div class="app"><div class="ico" style="background:#ebe8fa"><svg viewBox="0 0 24 24" stroke="#6a5acd"><path d="M9 3h6M10 3v6l-5 11h14l-5-11V3"/></svg></div><h3>Research Stations</h3><p>Reliable power and data transmission for remote research facilities, weather stations, and scientific outposts.</p></div>
  </div>
</section>

<section class="cta">
  <h2>Bereit für die Energie der Zukunft?</h2>
  <p>Entdecken Sie, wie varomind innovative Lösungen für erneuerbare Energien und<br>Kommunikation Ihre Prozesse transformieren können.</p>
  <span class="btn"><span class="dot"></span>Jetzt entdecken</span>
</section>

<footer class="footer">
  <div class="fbrand">varomind</div>
  <div class="social" aria-label="Soziale Netzwerke"><span></span><span></span><span></span><span></span></div>
  <div class="cols">
    <ul><h4>Lösungen</h4><li>Smart City</li><li>Kommunikation</li><li>Sport &amp; Freizeit</li><li>Verteidigung</li><li>Umwelt &amp; Agrar</li><li>Forschung &amp; Entwicklung</li></ul>
    <ul><h4>Technologie</h4><li>Helix-Windsysteme</li><li>Solarintegration</li><li>Drahtlose Datenübertragung</li><li>Energiespeicherung</li><li>Mesh-Netzwerke</li></ul>
    <ul><h4>Unternehmen</h4><li>Über uns</li><li>Führung</li><li>Karriere</li><li>Neuigkeiten</li><li>Kontakt</li></ul>
    <ul class="contact"><h4>Kontakt</h4>
      <li><svg viewBox="0 0 16 16"><path d="M8 15s5-5 5-9A5 5 0 003 6c0 4 5 9 5 9z"/><circle cx="8" cy="6" r="1.6"/></svg>Lindenhof 48, 10437 Berlin, Germany</li>
      <li><svg viewBox="0 0 16 16"><path d="M3 2h3l1.5 3.5-2 1.2a8 8 0 003.8 3.8l1.2-2L14 10v3a1 1 0 01-1 1A11 11 0 012 3a1 1 0 011-1z"/></svg>+49 30 5550182</li>
      <li><svg viewBox="0 0 16 16"><rect x="2" y="3.5" width="12" height="9" rx="1"/><path d="M2 4l6 5 6-5"/></svg>hallo@varomind.example</li>
    </ul>
  </div>
</footer>
<div class="legal"><span>© 2025 varomind. Alle Rechte vorbehalten.</span><div><span>Datenschutzerklärung</span><span>Nutzungsbedingungen</span><span>Cookie-Richtlinie</span></div></div>
<div class="theme"></div>
</body>
</html>
```